Stationary design and implementation for Swedish IT company

Hi,

I'm looking for a design and statiionary for my company (www.lumaverk.example).

Lumaverk is an innovative company with four core values:
- Entrepreneurial; we take risks and the responsibility to create value
- Awarding; we work with fun and have added value to our relationships
- Innovation; we're creative and introduce new solutions
- Respect; we work with respect for our environment based on values instead of red tape

The required stationary should include:
- Powerpoint template
- Word templates
- Business card design
- e-mail signature

Please visit our site for more details.
Updates

Hi - please read (PRIORITY!),

You have been involved in one my projects. 

As it seems there is something seriously wrong with the participation payments at ArtFolkHub. 

I have send invites with participation payments to reward designers for there work. It has been reported that these invitations resulted in expired messages, and payments have NOT been made. The money is withdrawn from my account and NOT paid to designers. This is a real shame when people do not get rewarded for the work done and the money is gone.

When you got an invitation with participation payment could you please let me know if the payment has actually been made? You can contact me at hmelsted@lumaverk.example.

I'm trying to get this clarified with ArtFolkHub.

Grt, Joost

Target Market(s)

Our market is IT and professional service in Sweden and other Nordics countries (Danmark, Norway, Finland).

Industry/Entity Type

Environment

Requirements
Must have
• Project delivery should include:
- Powerpoint template with title and content pages
- Standard letter (Word template)
- Standard invoice (Word template)
- Business card
- e-mail signature
Should not have
• Please await a logo to be attached (almost done).

```html
<!DOCTYPE html>
<html lang="en">
<head>
<meta charset="utf-8">
<title>Lumaverk Letterhead</title>
<link rel="stylesheet" href="https://fonts.googleapis.com/css2?family=Source+Sans+3:ital,wght@0,400;0,600;1,400&display=swap">
<style>
  :root {
    --brand-blue: #3a72c6;
    --brand-blue-dark: #2b5fb0;
    --brand-navy: #213f8c;
    --muted-grey: #a9a9a9;
    --paper: #ffffff;
  }
  * { margin: 0; padding: 0; box-sizing: border-box; }
  html, body { width: 928px; height: 1200px; overflow: hidden; background: var(--paper); }
  .letterhead {
    position: relative;
    width: 928px;
    height: 1200px;
    background: var(--paper);
    font-family: "Source Sans 3", "Myriad Pro", Arial, sans-serif;
  }
  .sender-tab {
    position: absolute;
    left: 0;
    top: 46px;
    width: 226px;
    height: 44px;
  }
  .sender-tab svg { position: absolute; inset: 0; }
  .sender-name {
    position: absolute;
    left: 32px;
    top: 8px;
    color: #fff;
    font-size: 15.5px;
    line-height: 1;
    white-space: nowrap;
  }
  .sender-location {
    position: absolute;
    left: 33px;
    top: 27px;
    color: #dfe8f7;
    font-size: 6.5px;
    font-style: italic;
    white-space: nowrap;
  }
  .contact {
    position: absolute;
    left: 245px;
    top: 51px;
    color: var(--brand-blue);
    font-size: 13px;
    line-height: 18px;
  }
  .brand {
    position: absolute;
    right: 44px;
    top: 40px;
    display: flex;
    align-items: center;
    gap: 14px;
  }
  .brand-dot {
    width: 34px;
    height: 34px;
    border-radius: 50%;
    background: var(--brand-navy);
  }
  .brand-name {
    color: var(--brand-navy);
    font-size: 52px;
    font-weight: 600;
    line-height: 1;
    letter-spacing: -0.5px;
  }
  .footer {
    position: absolute;
    left: 0;
    right: 0;
    top: 1130px;
    text-align: center;
  }
  .footer-url {
    color: var(--brand-blue);
    font-size: 19.5px;
    line-height: 1;
  }
  .footer-values {
    margin-top: 6px;
    color: var(--muted-grey);
    font-size: 12px;
    letter-spacing: 0.2px;
    text-transform: uppercase;
  }
</style>
</head>
<body>
  <main class="letterhead">
    <header>
      <div class="sender-tab">
        <svg width="226" height="44" viewBox="0 0 226 44" aria-hidden="true">
          <defs>
            <linearGradient id="tabFill" x1="0" y1="0" x2="0" y2="1">
              <stop offset="0" stop-color="#4680d3"/>
              <stop offset="1" stop-color="#2f64b5"/>
            </linearGradient>
          </defs>
          <path d="M0 0 H210 L226 22 L210 44 H0 Z" fill="url(#tabFill)"/>
        </svg>
        <span class="sender-name">Joost Melsted, Owner</span>
        <span class="sender-location">Stockholm Area Sweden</span>
      </div>
      <address class="contact" style="font-style: normal;">
        <div>[M] hmelsted@lumaverk.example</div>
        <div>[T] +46 70 555 0142</div>
      </address>
      <div class="brand">
        <span class="brand-dot" aria-hidden="true"></span>
        <span class="brand-name">Lumaverk</span>
      </div>
    </header>

    <footer class="footer">
      <div class="footer-url">www.lumaverk.example</div>
      <div class="footer-values">Entrepreneurial • Awarding • Innovation • Respect</div>
    </footer>
  </main>
</body>
</html>
```